Career-focused learning application platform

We have a K-12 learning application platform designed for grades 6-12 that needs user interface improvements that provide a positive experience for all users (teachers and students). The learning platform provides career-focused math curriculum and career exploration resources. We would like to improve the user-interface with engaging design elements without taking away from the functionality and performance of the platform.

```html
<!DOCTYPE html>
<html lang="en">
<head>
<meta charset="utf-8">
<title>Tallyworks – Learning Platform Screens</title>
<link href="https://fonts.googleapis.com/css2?family=Poppins:wght@400;500;600;700&display=swap" rel="stylesheet">
<style>
:root{
  --bg:#ffffff;
  --screen:#f6f6f8;
  --card:#ffffff;
  --ink:#1d1d2b;
  --muted:#8a8a96;
  --line:#e6e6ec;
  --orange:#f06a35;
  --red:#e5473b;
  --sky:#28a8f0;
  --violet:#4b3fe0;
  --navy:#1f3a68;
  --plum:#7a3561;
  --teal:#2f6f6b;
  --midnight:#1d2f5e;
  --folder:#f5c94a;
  --due:#ef4444;
  --pale-blue:#d6eefb;
  --art-deep:#2d3592;
  --art-mid:#4a5fc4;
}
*{box-sizing:border-box;margin:0;padding:0}
html,body{width:1200px;height:342px;overflow:hidden;background:var(--bg);font-family:"Poppins",sans-serif;color:var(--ink)}
.screen{position:absolute;background:var(--screen);border:1px solid var(--line);border-radius:4px;overflow:hidden}
.abs{position:absolute}
.login{left:16px;top:16px;width:381px;height:214px;background:#f4f4f6}
.login .art-side{left:190px;top:0;width:191px;height:214px;background:var(--pale-blue)}
.login .art{left:20px;top:46px;width:151px;height:122px;border-radius:10px;background:linear-gradient(150deg,var(--art-mid) 0%,var(--art-deep) 55%,#c9d7f2 100%)}
h1.signin-title{left:49px;top:52px;font-size:5px;font-weight:600}
.btn{position:absolute;display:flex;align-items:center;justify-content:center;font-size:3px;font-weight:500;border-radius:1px;white-space:nowrap}
.btn.sso-a{left:49px;top:62px;width:44px;height:12px;background:var(--red);color:#fff}
.btn.sso-b{left:97px;top:62px;width:45px;height:12px;background:var(--sky);color:#fff}
.divider{left:49px;top:86px;width:93px;border-top:.5px solid var(--line)}
.divider span{position:absolute;left:50%;top:-2px;transform:translateX(-50%);background:#f4f4f6;padding:0 3px;font-size:2.4px;color:var(--muted);white-space:nowrap}
.label{font-size:2.6px;font-weight:500}
.field{width:93px;height:11px;background:#fff;border:.5px solid var(--line);font-size:2.2px;color:var(--muted);display:flex;align-items:center;padding-left:12px}
.field i{position:absolute;left:4px;top:4px;width:3px;height:3px;background:#9a9aa6;border-radius:.5px}
.remember{left:49px;top:137px;font-size:2.2px;color:var(--muted)}
.btn.primary{background:var(--violet);color:#fff}
.btn.outline{border:.5px solid var(--violet);color:var(--violet);background:#fff}

.topbar{left:0;top:0;width:100%;height:15px;background:#fff;border-bottom:.5px solid var(--line)}
.brand{left:12px;top:4.5px;display:flex;align-items:center;gap:2px;font-size:4.4px;color:var(--orange);font-weight:500}
.brand b{width:3px;height:3px;background:var(--orange);border-radius:50%}
.nav{left:145px;top:5.5px;display:flex;gap:10px;font-size:2.6px;font-weight:600;white-space:nowrap}
.nav .active{color:var(--ink);position:relative}
.nav .active:after{content:"";position:absolute;left:0;right:0;top:7px;height:.8px;background:var(--orange)}
.user{right:12px;top:4px;display:flex;align-items:center;gap:3px;font-size:2.4px}
.user b{width:7px;height:7px;border-radius:50%;background:#b0563f}

.home{left:413px;top:16px;width:381px;height:311px}
.section-title{font-size:4.4px;font-weight:700}
.spot-bar{left:66px;top:35px;width:248px;height:12px;background:var(--orange);color:#fff;font-size:3px;font-weight:600;padding:3.5px 7px;border-radius:1.5px 1.5px 0 0}
.spot-body{left:66px;top:47px;width:248px;height:81px;background:#fff}
.spot-text{left:7px;top:8px;width:110px;font-size:2.3px;color:var(--muted);line-height:1.5}
.spot-text h3{font-size:2.6px;color:var(--ink);font-weight:600;margin-bottom:3px}
.earn{left:7px;top:40px;font-size:2.5px;font-weight:600}
.earn-row{left:7px;top:46px;display:flex;gap:14px}
.earn-row div{font-size:2px;color:var(--muted)}
.earn-row strong{display:block;font-size:4px;color:var(--violet);font-weight:600}
.btn.learn{left:7px;top:62px;width:44px;height:12px}
.spot-photo{left:127px;top:0;width:121px;height:81px;background:linear-gradient(135deg,#8a1f24,#2b3350 55%,#c63a3a)}
.class-card{position:absolute;top:149px;width:58px;height:65px;background:#fff;border-radius:1.5px;overflow:hidden}
.class-card .head{height:20px;color:#fff;padding:3px 4px;font-size:2.6px;font-weight:600;line-height:1.4}
.class-card .head small{display:block;font-size:2px;font-weight:400;opacity:.85}
.class-card svg{position:absolute;left:19px;top:27px}
.class-card .foot{position:absolute;bottom:0;left:0;right:0;height:10px;color:#fff;font-size:2.6px;font-weight:600;display:flex;align-items:center;justify-content:center}
.c1 .head,.c1 .foot{background:var(--navy)}
.c2 .head,.c2 .foot{background:var(--plum)}
.c3 .head,.c3 .foot{background:var(--teal)}
.c4 .head,.c4 .foot{background:var(--midnight)}
.subtle{font-size:2.3px;color:var(--muted)}
table.lessons{position:absolute;left:66px;top:243px;width:248px;border-collapse:collapse;background:#fff;font-size:2.4px}
table.lessons th{background:#eeeef2;text-align:left;height:11px;font-weight:600}
table.lessons td{height:10px;border-top:.5px solid var(--line)}
table.lessons th:first-child,table.lessons td:first-child{padding-left:8px;width:51px}
table.lessons td:nth-child(2){width:143px}
.due{color:var(--due)}

.cls{left:811px;top:16px;width:381px;height:214px}
.banner{left:66px;top:35px;width:248px;height:20px;background:var(--navy);border-radius:1.5px;color:#fff;padding:3px 4px;font-size:2.6px;font-weight:600}
.banner small{display:block;font-size:2px;font-weight:400;opacity:.85;line-height:1.4}
.btn.ghost{top:6px;width:34px;height:8px;background:#fff;color:var(--ink);font-size:2.3px}
.tabs{left:66px;top:63px;display:flex;gap:12px;font-size:2.8px;color:var(--muted)}
.tabs .on{color:var(--orange);border-bottom:.6px solid var(--orange)}
.list{left:66px;top:72px;width:248px;height:109px;background:#fff}
.list-head{height:12px;background:#eeeef2;font-size:2.8px;font-weight:600;padding:4px 8px;position:relative}
.btn.add{left:205px;top:2px;width:34px;height:8px;background:#d8d8de;color:var(--ink);font-size:2.3px}
.row{position:relative;height:24.3px;border-top:.5px solid var(--line)}
.row svg{position:absolute;left:8px;top:4px}
.row .txt{position:absolute;left:28px;top:4px;width:120px;font-size:2.6px;font-weight:600}
.row .txt p{font-size:1.9px;font-weight:400;color:var(--muted);line-height:1.4;margin-top:1px}
.row .when{position:absolute;left:202px;top:5px;font-size:2.3px;color:var(--due);white-space:nowrap}
.row .btn{left:202px;top:11px;width:25px;height:7px;background:var(--navy);color:#fff;font-size:2.1px}
</style>
</head>
<body>

<section class="screen login" aria-label="Sign in">
  <div class="abs art-side"><div class="abs art" role="img" aria-label="Illustration of math books, a calculator and numbers for trigonometry"></div></div>
  <h1 class="abs signin-title">Sign in with your school account</h1>
  <span class="btn sso-a">Orbit ID</span>
  <span class="btn sso-b">Keystone</span>
  <div class="abs divider"><span>Or Continue With</span></div>
  <div class="abs label" style="left:49px;top:97px">Email Address</div>
  <div class="abs field" style="left:49px;top:102px"><i></i>Your email</div>
  <div class="abs label" style="left:49px;top:118px">Password</div>
  <div class="abs field" style="left:49px;top:123px"><i></i>Your password</div>
  <div class="abs remember">Remember me</div>
  <span class="btn primary" style="left:49px;top:149px;width:44px;height:12px">Sign in</span>
  <span class="btn outline" style="left:97px;top:149px;width:45px;height:12px">Sing up</span>
</section>

<section class="screen home" aria-label="Home dashboard">
  <header class="abs topbar">
    <div class="abs brand"><b></b>Tallyworks</div>
    <nav class="abs nav"><span class="active">Home</span><span>Career Tools</span><span>Classes</span><span>Assessments</span></nav>
    <div class="abs user">jo@tallyworks.edu<b></b></div>
  </header>
  <h2 class="abs section-title" style="left:66px;top:28px">CAREER SPOTLIGHT</h2>
  <div class="abs spot-bar">Plumbers, Pipefitters, &amp; Steamfitters</div>
  <div class="abs spot-body">
    <div class="abs spot-text"><h3>What they do</h3>Install and repair pipe systems that carry water, steam and gas in homes, plants and large buildings.</div>
    <div class="abs earn">Earnings</div>
    <div class="abs earn-row">
      <div>Low end<strong>$33,460</strong></div>
      <div>Median<strong>$56,330</strong></div>
      <div>High end<strong>$98,990</strong></div>
    </div>
    <span class="btn primary learn">Learn more</span>
    <div class="abs spot-photo" role="img" aria-label="Photo of industrial pipes and valves in a plant room"></div>
  </div>
  <h2 class="abs section-title" style="left:66px;top:141px">CLASSES</h2>
  <div class="class-card c1" style="left:66px"><div class="head">Math Teacher<small>Period 1<br>8th Grade Math / Pre-Algebra</small></div>
    <svg width="20" height="22" viewBox="0 0 20 22"><rect x="3" y="0" width="13" height="8" fill="#1f3a68"/><rect x="0" y="6" width="20" height="15" rx="1" fill="#f5c94a"/><rect x="7" y="12" width="6" height="1.2" fill="#1f3a68"/></svg>
    <div class="foot">Go To Class</div></div>
  <div class="class-card c2" style="left:129px"><div class="head">Math Teacher<small>Period 1<br>8th Grade Math / Pre-Algebra</small></div>
    <svg width="20" height="22" viewBox="0 0 20 22"><rect x="3" y="0" width="13" height="8" fill="#7a3561"/><rect x="0" y="6" width="20" height="15" rx="1" fill="#f5c94a"/><rect x="7" y="12" width="6" height="1.2" fill="#7a3561"/></svg>
    <div class="foot">Go To Class</div></div>
  <div class="class-card c3" style="left:193px"><div class="head">Math Teacher<small>Period 1<br>8th Grade Math / Pre-Algebra</small></div>
    <svg width="20" height="22" viewBox="0 0 20 22"><rect x="3" y="0" width="13" height="8" fill="#2f6f6b"/><rect x="0" y="6" width="20" height="15" rx="1" fill="#f5c94a"/><rect x="7" y="12" width="6" height="1.2" fill="#2f6f6b"/></svg>
    <div class="foot">Go To Class</div></div>
  <div class="class-card c4" style="left:256px"><div class="head">Math Teacher<small>Period 1<br>8th Grade Math / Pre-Algebra</small></div>
    <svg width="20" height="22" viewBox="0 0 20 22"><rect x="3" y="0" width="13" height="8" fill="#1d2f5e"/><rect x="0" y="6" width="20" height="15" rx="1" fill="#f5c94a"/><rect x="7" y="12" width="6" height="1.2" fill="#1d2f5e"/></svg>
    <div class="foot">Go To Class</div></div>
  <h2 class="abs section-title" style="left:66px;top:226px">UPCOMING LESSONS</h2>
  <div class="abs subtle" style="left:66px;top:233px">Lesson due up to the next 7 days</div>
  <table class="lessons">
    <tr><th>Class</th><th>Lesson</th><th>Due</th></tr>
    <tr><td>Period 1</td><td>1.1 - Translations</td><td class="due">October 15th at 15:59 PM</td></tr>
    <tr><td>Period 1</td><td>2.1 - Operations With Rational Numbers</td><td class="due">October 15th at 15:59 PM</td></tr>
    <tr><td>Period 1</td><td>3.1 - Parallel Lines And Transversals</td><td class="due">October 15th at 15:59 PM</td></tr>
    <tr><td>Period 1</td><td>3.3 - Angle Relationship In Triangles</td><td class="due">October 15th at 15:59 PM</td></tr>
  </table>
</section>

<section class="screen cls" aria-label="Class detail">
  <header class="abs topbar">
    <div class="abs brand"><b></b>Tallyworks</div>
    <nav class="abs nav"><span class="active">Home</span><span>Career Tools</span><span>Classes</span><span>Assessments</span></nav>
    <div class="abs user">jo@tallyworks.edu<b></b></div>
  </header>
  <div class="abs subtle" style="left:75px;top:30px;color:var(--ink);font-weight:500">Browse all classes</div>
  <div class="abs banner">Math Teacher<small>Period 1<br>8th Grade Math / Pre-Algebra</small>
    <span class="btn ghost" style="left:172px">Roster Class</span>
    <span class="btn ghost" style="left:210px">Class Settings</span>
  </div>
  <div class="abs tabs"><span class="on">Lessons</span><span>Scores</span></div>
  <div class="abs list">
    <div class="list-head">Upcoming Lessons<span class="btn add">Add Lesson</span></div>
    <div class="row"><svg width="16" height="16" viewBox="0 0 20 20"><rect x="2" y="0" width="14" height="8" fill="#1f3a68"/><rect x="0" y="6" width="20" height="14" rx="1" fill="#f5c94a"/><rect x="7" y="12" width="6" height="1.2" fill="#1f3a68"/></svg>
      <div class="txt">1.1 - Translations<p>Practice the core ideas of this lesson with guided examples and short checks.</p></div>
      <div class="when">October 15th at 15:59 PM</div><span class="btn">Begin Lesson</span></div>
    <div class="row"><svg width="16" height="16" viewBox="0 0 20 20"><rect x="2" y="0" width="14" height="8" fill="#1f3a68"/><rect x="0" y="6" width="20" height="14" rx="1" fill="#f5c94a"/><rect x="7" y="12" width="6" height="1.2" fill="#1f3a68"/></svg>
      <div class="txt">2.1 - Operations With Rational Numbers<p>Practice the core ideas of this lesson with guided examples and short checks.</p></div>
      <div class="when">October 15th at 15:59 PM</div><span class="btn">Begin Lesson</span></div>
    <div class="row"><svg width="16" height="16" viewBox="0 0 20 20"><rect x="2" y="0" width="14" height="8" fill="#1f3a68"/><rect x="0" y="6" width="20" height="14" rx="1" fill="#f5c94a"/><rect x="7" y="12" width="6" height="1.2" fill="#1f3a68"/></svg>
      <div class="txt">3.1 - Parallel Lines And Transversals<p>Practice the core ideas of this lesson with guided examples and short checks.</p></div>
      <div class="when">October 15th at 15:59 PM</div><span class="btn">Begin Lesson</span></div>
    <div class="row"><svg width="16" height="16" viewBox="0 0 20 20"><rect x="2" y="0" width="14" height="8" fill="#1f3a68"/><rect x="0" y="6" width="20" height="14" rx="1" fill="#f5c94a"/><rect x="7" y="12" width="6" height="1.2" fill="#1f3a68"/></svg>
      <div class="txt">3.3 - Angle Relationship In Triangles<p>Practice the core ideas of this lesson with guided examples and short checks.</p></div>
      <div class="when">October 15th at 15:59 PM</div><span class="btn">Begin Lesson</span></div>
  </div>
</section>

</body>
</html>
```